Norvessa Imports Busisness cards and logo

Norvessa imports is a brand new wholesale company located in Londonderry, New Hampshire dedicated to finding unique products from around the world.
Licensed to sell wine and spirits in the state and also authorized distributors of Velvet Lantern Design, a manufacturer of girls and women shoes. Other products that we are currently trying to import are cheese and frozen food from Spain.
We would like a design that portraits our diversity of products and wholesale capabilities

Reason: Still undecided. Waiting for more feedback from the poll Thanks

```html
<!DOCTYPE html>
<html lang="en">
<head>
<meta charset="utf-8">
<title>Norvessa Imports – Business Card</title>
<link rel="stylesheet" href="https://fonts.googleapis.com/css2?family=Open+Sans:ital,wght@0,400;0,600;0,700;1,400;1,700&display=swap">
<style>
  :root {
    --backdrop: #e9e7e3;
    --card-white: #ffffff;
    --card-grey-top: #f4f4f4;
    --green-dark: #3f7a3a;
    --green-light: #7cb84a;
    --brand-green: #3f8f2a;
    --swoosh-grey: #9a9a9c;
    --icon-green: #4f8a3e;
    --text-white: #ffffff;
    --shadow: rgba(0, 0, 0, 0.18);
  }
  * { margin: 0; padding: 0; box-sizing: border-box; }
  html, body {
    width: 1200px;
    height: 900px;
    overflow: hidden;
    background: var(--backdrop);
    font-family: "Open Sans", Arial, sans-serif;
  }
  .canvas { position: relative; width: 1200px; height: 900px; }

  .card {
    position: absolute;
    width: 600px;
    height: 343px;
    border-radius: 26px;
    overflow: hidden;
    background: linear-gradient(160deg, var(--card-white) 0%, var(--card-grey-top) 100%);
    box-shadow: 0 10px 28px var(--shadow);
  }
  .card--front { left: 80px; top: 70px; }
  .card--back  { left: 520px; top: 490px; }

  .brand {
    position: absolute;
    display: flex;
    align-items: center;
    gap: 14px;
  }
  .brand__dot {
    width: 46px; height: 46px;
    border-radius: 50%;
    background: var(--brand-green);
  }
  .brand__name {
    font-weight: 700;
    font-size: 40px;
    line-height: 1.2;
    color: var(--brand-green);
    letter-spacing: -0.5px;
  }
  .card--front .brand { left: 110px; top: 142px; }
  .card--back .brand  { left: 62px;  top: 44px; }
  .card--back .brand__name { font-size: 32px; }
  .card--back .brand__dot { width: 36px; height: 36px; }

  .back-art { position: absolute; inset: 0; width: 100%; height: 100%; }

  .holder {
    position: absolute;
    left: 36px;
    top: 272px;
    color: var(--text-white);
  }
  .holder__name { font-size: 21px; font-weight: 700; font-style: italic; line-height: 1.1; }
  .holder__role { font-size: 18px; font-style: italic; font-weight: 400; line-height: 1.3; }

  .contacts {
    position: absolute;
    left: 398px;
    top: 172px;
    list-style: none;
    color: var(--text-white);
    font-size: 12.5px;
    line-height: 1.25;
  }
  .contacts li { display: flex; align-items: flex-start; gap: 7px; margin-bottom: 5px; }
  .contacts li:first-child { margin-bottom: 8px; }
  .contacts li:last-child { margin-bottom: 0; }
  .contacts svg { flex: none; width: 13px; height: 13px; margin-top: 1px; }
</style>
</head>
<body>
<main class="canvas">

  <section class="card card--front" aria-label="Card front">
    <div class="brand">
      <span class="brand__dot"></span>
      <span class="brand__name">Norvessa Imports</span>
    </div>
  </section>

  <section class="card card--back" aria-label="Card back">
    <svg class="back-art" viewBox="0 0 600 343" preserveAspectRatio="none" aria-hidden="true">
      <defs>
        <linearGradient id="bandGreen" x1="0" y1="1" x2="1" y2="0">
          <stop offset="0" stop-color="#3f7a3a"/>
          <stop offset="1" stop-color="#7cb84a"/>
        </linearGradient>
      </defs>
      <path class="swoosh" d="M0,214 Q190,238 600,22 Q210,252 0,229 Z" fill="#9a9a9c"/>
      <path class="green-band" d="M0,240 Q200,260 600,40 L600,343 L0,343 Z" fill="url(#bandGreen)"/>
    </svg>

    <div class="brand">
      <span class="brand__dot"></span>
      <span class="brand__name">Norvessa Imports</span>
    </div>

    <div class="holder">
      <p class="holder__name">Daniel Reyes</p>
      <p class="holder__role">Owner / C.E.O</p>
    </div>

    <ul class="contacts">
      <li>
        <svg viewBox="0 0 14 14"><circle cx="7" cy="7" r="7" fill="#fff"/><path d="M3.5 7.5 7 4.2l3.5 3.3V10.5h-7z" fill="#4f8a3e"/></svg>
        <span>Suite # 118, Kell Bldg,<br>NH 03053</span>
      </li>
      <li>
        <svg viewBox="0 0 14 14"><circle cx="7" cy="7" r="7" fill="#fff"/><path d="M4.5 3.5h1.8l.7 2-1 .8a5 5 0 0 0 2 2l.8-1 2 .7v1.8c-3.5.3-6.6-2.8-6.3-6.3z" fill="#4f8a3e"/></svg>
        <span>603-555-0142</span>
      </li>
      <li>
        <svg viewBox="0 0 14 14"><circle cx="7" cy="7" r="7" fill="#fff"/><rect x="5" y="3" width="4" height="8" rx="0.8" fill="#4f8a3e"/></svg>
        <span>603-555-0187</span>
      </li>
      <li>
        <svg viewBox="0 0 14 14"><circle cx="7" cy="7" r="7" fill="#fff"/><rect x="3.5" y="5.5" width="7" height="4.5" fill="#4f8a3e"/><rect x="5" y="3.5" width="4" height="2" fill="#4f8a3e"/></svg>
        <span>603-555-0163</span>
      </li>
      <li>
        <svg viewBox="0 0 14 14"><circle cx="7" cy="7" r="7" fill="#fff"/><rect x="3.5" y="4.5" width="7" height="5" fill="#4f8a3e"/><path d="M3.5 4.5 7 7.5l3.5-3" stroke="#fff" stroke-width="0.8" fill="none"/></svg>
        <span>hello@norvessaimports.com</span>
      </li>
      <li>
        <svg viewBox="0 0 14 14"><circle cx="7" cy="7" r="7" fill="#fff"/><circle cx="7" cy="7" r="3.8" fill="none" stroke="#4f8a3e" stroke-width="1"/><path d="M3.2 7h7.6M7 3.2v7.6" stroke="#4f8a3e" stroke-width="0.8"/></svg>
        <span>www.norvessaimports.com</span>
      </li>
    </ul>
  </section>

</main>
</body>
</html>
```